Retail Fitness Store requires Flyer for Women's Mini Marathon

Our retail store will be present as a vendor at a collection point for a women's mini marathon, target audience is 18-40
http://www.larkwomenstenkrun.ie

We need you to design a elegant flyer to be handed out on the day to advertise our fitness store focusing on female products. the following information needs to be shown, business name, address, contact number.

What we do, you can use images or text for the following, mini bands, power bands, rollers, knee sleeves, aerobic bars, vinyl dumbbells, hula hoops, women gloves, weightlifting belts, compression bv sports bras, compression tops / bottoms, ab rollers, pilates, yoga, fitness books.

Also mention we do a large range of other fitness equipment for strength training, olympic lifting, power lifting.

All information can be taking from our website www.q5movewell.com

Target Market(s)

18 - 40 female fitness enthusiats

Industry/Entity Type

Health And Wellness

Font styles to use
Sans Serif

Requirements
Must have
• Q5 Movewell Strore
• 7 & 8 Glenmora Mews
• Tallis Row Dublin
• 00353 1 618 2094
• www.q5movewell.com
Nice to have
• nice colour - a few images -
Should not have
• dark colours - image son men training or heavy weights
• please feel free to change the back ground colour of the logo that has been uploaded.

```html
<!DOCTYPE html>
<html lang="en">
<head>
<meta charset="utf-8">
<title>Q5 Movewell Store – Female Fitness Products Flyer</title>
<link rel="stylesheet" href="https://fonts.googleapis.com/css2?family=Open+Sans:wght@400;600;700&family=Roboto+Condensed:wght@700&family=Oswald:wght@500&display=swap">
<style>
  :root {
    --page-bg: #e9e6e1;
    --flyer-black: #141414;
    --paper: #ffffff;
    --brand-blue: #1a9fd6;
    --band-light: #22b2e6;
    --band-dark: #0f7cb3;
    --ink: #222222;
    --light-text: #ffffff;
    --skin-light: #f3e6dc;
    --skin-mid: #d9b49a;
  }
  * { box-sizing: border-box; margin: 0; padding: 0; }
  html, body { width: 964px; height: 1200px; overflow: hidden; }
  body { background: var(--page-bg); font-family: "Open Sans", sans-serif; position: relative; }

  .flyer {
    position: absolute; left: 82px; top: 35px;
    width: 800px; height: 1130px;
    background: var(--flyer-black);
  }

  .hero {
    position: absolute; left: 21px; top: 29px;
    width: 758px; height: 533px;
    background: var(--paper);
    overflow: hidden;
  }
  .hero-photo {
    position: absolute; left: 30px; top: 30px; width: 700px; height: 503px;
    background: radial-gradient(ellipse at 62% 55%, var(--skin-mid) 0%, var(--skin-light) 45%, var(--paper) 75%);
  }
  .hero-title {
    position: absolute; left: 37px; top: 20px;
    font-weight: 700; font-size: 32px; color: var(--brand-blue); letter-spacing: -0.2px;
  }
  .hero-subtitle {
    position: absolute; left: 40px; top: 68px;
    font-size: 19px; color: var(--ink);
  }
  .shop-info { position: absolute; left: 30px; top: 402px; width: 292px; }
  .shop-info h2 {
    font-family: "Oswald", sans-serif; font-weight: 500;
    font-size: 14.5px; color: var(--brand-blue); letter-spacing: 0.3px;
  }
  .shop-info p {
    margin-top: 7px; font-size: 12px; line-height: 15.4px;
    color: var(--ink); text-align: justify;
  }
  .contact {
    position: absolute; right: 29px; top: 480px; text-align: right;
    font-size: 14.5px; color: var(--ink); line-height: 25px;
  }

  .headline-band {
    position: absolute; left: 21px; top: 562px;
    width: 758px; height: 271px;
    background: radial-gradient(ellipse at 50% 25%, var(--band-light) 0%, var(--band-dark) 85%);
    text-align: center; color: var(--light-text);
    font-family: "Roboto Condensed", sans-serif; font-weight: 700;
    text-shadow: 2px 3px 4px rgba(0,0,0,0.35);
  }
  .headline-band h1 {
    padding-top: 19px; font-size: 74px; line-height: 73px; letter-spacing: 2.5px;
  }
  .headline-band .web {
    margin-top: 20px; font-size: 48px; letter-spacing: 3px;
  }

  .products { position: absolute; left: 30px; top: 852px; color: var(--light-text); }
  .products h3 {
    font-family: "Oswald", sans-serif; font-weight: 500; font-size: 22px; letter-spacing: 0.3px;
  }
  .product-list {
    list-style: none; margin-top: 12px;
    display: grid; grid-template-columns: 203px auto; row-gap: 0;
    font-size: 16px; line-height: 23.4px;
  }
  .product-list li { display: flex; align-items: center; white-space: nowrap; }
  .product-list li.wide { grid-column: 1 / 3; }
  .product-list li svg { width: 17px; height: 17px; margin-right: 6px; flex: none; }

  .brand {
    position: absolute; left: 525px; top: 905px; width: 250px;
    display: flex; align-items: center; gap: 12px;
    font-family: "Open Sans", sans-serif; font-weight: 700; font-size: 32px;
    color: var(--brand-blue); white-space: nowrap;
  }
  .brand-dot { width: 26px; height: 26px; border-radius: 50%; background: var(--brand-blue); flex: none; }

  .call-bar {
    position: absolute; left: 32px; top: 1082px; width: 396px; height: 14px;
    background: linear-gradient(90deg, var(--band-dark), var(--band-light) 55%, var(--band-dark));
  }
  .call {
    position: absolute; right: 43px; top: 1058px;
    font-family: "Roboto Condensed", sans-serif; font-weight: 700;
    font-size: 46px; color: var(--light-text); line-height: 50px;
  }
  .call small { font-size: 36px; }
</style>
</head>
<body>
<main class="flyer">
  <section class="hero">
    <div class="hero-photo" role="img" aria-label="Photo of a smiling young woman in sportswear doing a push-up on a white floor"></div>
    <div class="hero-title">women's marathon products</div>
    <div class="hero-subtitle">Easy Returns Policy</div>
    <div class="shop-info">
      <h2>EASY ONLINE SHOPPING</h2>
      <p>Our physical store is located in Dublin's city centre. Here you can try out and browse the largest selection of fitness gear around, including kettlebells, weightlifting bars, plates and weights, SLX and cross-fit equipment, brand name athletic footwear, nutritional products and more!</p>
    </div>
    <div class="contact">
      <div>e. info@q5movewell.com</div>
      <div>Unit 7/8 Glenmora Mews, Tallis Row, Dublin 8</div>
    </div>
  </section>

  <section class="headline-band">
    <h1>FEMALE FITNESS<br>PRODUCTS STORE</h1>
    <div class="web">www.q5movewell.com</div>
  </section>

  <section class="products">
    <h3>OUR PRODUCTS ARE...</h3>
    <ul class="product-list">
      <li><svg viewBox="0 0 20 20"><circle cx="10" cy="10" r="9" fill="#1a9fd6"/><circle cx="10" cy="10" r="6" fill="#cfefff"/><path d="M8 6l5 4-5 4z" fill="#0f7cb3"/></svg>Mini Bands</li>
      <li><svg viewBox="0 0 20 20"><circle cx="10" cy="10" r="9" fill="#1a9fd6"/><circle cx="10" cy="10" r="6" fill="#cfefff"/><path d="M8 6l5 4-5 4z" fill="#0f7cb3"/></svg>Power Bands</li>
      <li><svg viewBox="0 0 20 20"><circle cx="10" cy="10" r="9" fill="#1a9fd6"/><circle cx="10" cy="10" r="6" fill="#cfefff"/><path d="M8 6l5 4-5 4z" fill="#0f7cb3"/></svg>Rollers</li>
      <li><svg viewBox="0 0 20 20"><circle cx="10" cy="10" r="9" fill="#1a9fd6"/><circle cx="10" cy="10" r="6" fill="#cfefff"/><path d="M8 6l5 4-5 4z" fill="#0f7cb3"/></svg>Knee Sleeves</li>
      <li><svg viewBox="0 0 20 20"><circle cx="10" cy="10" r="9" fill="#1a9fd6"/><circle cx="10" cy="10" r="6" fill="#cfefff"/><path d="M8 6l5 4-5 4z" fill="#0f7cb3"/></svg>Aerobic Bars</li>
      <li><svg viewBox="0 0 20 20"><circle cx="10" cy="10" r="9" fill="#1a9fd6"/><circle cx="10" cy="10" r="6" fill="#cfefff"/><path d="M8 6l5 4-5 4z" fill="#0f7cb3"/></svg>Vinyl Dumbbells</li>
      <li><svg viewBox="0 0 20 20"><circle cx="10" cy="10" r="9" fill="#1a9fd6"/><circle cx="10" cy="10" r="6" fill="#cfefff"/><path d="M8 6l5 4-5 4z" fill="#0f7cb3"/></svg>Hula Hoops</li>
      <li><svg viewBox="0 0 20 20"><circle cx="10" cy="10" r="9" fill="#1a9fd6"/><circle cx="10" cy="10" r="6" fill="#cfefff"/><path d="M8 6l5 4-5 4z" fill="#0f7cb3"/></svg>Women Gloves</li>
      <li><svg viewBox="0 0 20 20"><circle cx="10" cy="10" r="9" fill="#1a9fd6"/><circle cx="10" cy="10" r="6" fill="#cfefff"/><path d="M8 6l5 4-5 4z" fill="#0f7cb3"/></svg>Weightlifting Belts</li>
      <li><svg viewBox="0 0 20 20"><circle cx="10" cy="10" r="9" fill="#1a9fd6"/><circle cx="10" cy="10" r="6" fill="#cfefff"/><path d="M8 6l5 4-5 4z" fill="#0f7cb3"/></svg>Compression Bv Sports Bras</li>
      <li class="wide"><svg viewBox="0 0 20 20"><circle cx="10" cy="10" r="9" fill="#1a9fd6"/><circle cx="10" cy="10" r="6" fill="#cfefff"/><path d="M8 6l5 4-5 4z" fill="#0f7cb3"/></svg>Compression Tops / Bottoms</li>
      <li class="wide"><svg viewBox="0 0 20 20"><circle cx="10" cy="10" r="9" fill="#1a9fd6"/><circle cx="10" cy="10" r="6" fill="#cfefff"/><path d="M8 6l5 4-5 4z" fill="#0f7cb3"/></svg>Ab Rollers, Pilates, Yoga, Fitness Books.</li>
    </ul>
  </section>

  <div class="brand"><span class="brand-dot"></span>Q5 Movewell</div>

  <div class="call-bar"></div>
  <div class="call"><small>Call:</small> 01 6182094</div>
</main>
</body>
</html>
```